Customer flyer

Hi there,

We need a flyer done for our father's business. It is called Harbor ledger and the flyer will be distributed to realtors in British Columbia. He lends money to realtors when they have sold a home from the time subjects are removed from the transaction to when the sale closes. He is looking for a modern, classy look with the following information:

"Harbor Ledger"

Realtor Pay Day upon Subject Removal

Did you know?

* Fees 100% tax deductable
* Same Day Service
* Confidential
* Low Rates

Your money from 583917 B.C. Ltd. and It can be directly deposited into your bank account or delivered to your office

For quote: call Glen Marsh 236 555 0147

This is a small business so he doesn't have a logo and has never needed to do promotions before as it's run on word of mouth for the past 10 years. We are open to all ideas and suggestions - he is a finance guy so looking to you for the creative side :)

Thank you!

I don't like the phrase Realtor Pay Day upon subject removal. I think I prefer "Realtors! Celebrate Your Home sales upon subject removal" . Your thoughts?

Thank you

```html
<!DOCTYPE html>
<html lang="en">
<head>
<meta charset="utf-8">
<title>Harbor Ledger – Realtor Pay Day</title>
<link rel="stylesheet" href="https://fonts.googleapis.com/css2?family=Roboto+Condensed:wght@800;900&family=Merriweather:wght@900&family=Questrial&display=swap">
<style>
  :root {
    --navy: #0c2c6a;
    --sky-light: #bfe3f5;
    --sky-mid: #5fb2e4;
    --sky-deep: #1f4fa8;
    --yellow: #fff200;
    --white: #ffffff;
    --red: #e3262c;
    --roof: #f07a3c;
    --note-pink: #e6a6b8;
    --note-teal: #7fc3c4;
  }
  * { margin: 0; padding: 0; box-sizing: border-box; }
  html, body { width: 848px; height: 1200px; overflow: hidden; background: var(--white); }
  .flyer {
    position: relative;
    width: 848px;
    height: 1200px;
    overflow: hidden;
    background:
      radial-gradient(ellipse 60% 40% at 15% 25%, rgba(255,255,255,.55), transparent 70%),
      radial-gradient(ellipse 50% 35% at 10% 75%, rgba(220,240,252,.5), transparent 70%),
      radial-gradient(ellipse 70% 60% at 95% 80%, var(--sky-deep), transparent 75%),
      linear-gradient(160deg, var(--sky-light) 0%, var(--sky-mid) 45%, #2f6cc0 80%, var(--sky-deep) 100%);
    font-family: "Questrial", sans-serif;
  }
  .brand-title {
    position: absolute;
    top: 22px; left: 0; width: 100%;
    text-align: center;
    font-family: "Roboto Condensed", sans-serif;
    font-weight: 900;
    font-size: 128px;
    line-height: 1;
    letter-spacing: -2px;
    color: var(--navy);
  }
  .hero-image {
    position: absolute;
    left: 363px; top: 160px;
    width: 480px; height: 340px;
  }
  .headline {
    position: absolute;
    left: 82px; top: 222px;
    font-family: "Merriweather", serif;
    font-weight: 900;
    font-size: 74px;
    line-height: 78px;
    color: var(--yellow);
  }
  .subline {
    position: absolute;
    left: 84px; top: 402px;
    font-family: "Roboto Condensed", sans-serif;
    font-weight: 800;
    font-size: 36px;
    line-height: 1;
    letter-spacing: -0.5px;
    color: var(--navy);
  }
  .intro {
    position: absolute;
    top: 508px; left: 0; width: 100%;
    text-align: center;
    font-family: "Merriweather", serif;
    font-weight: 900;
    font-size: 54px;
    line-height: 1;
    color: var(--white);
  }
  .benefits {
    position: absolute;
    top: 583px; left: 0; width: 100%;
    list-style: none;
    text-align: center;
  }
  .benefits li {
    font-size: 48px;
    line-height: 57px;
    color: var(--yellow);
  }
  .benefits li::before {
    content: "\273B";
    color: var(--red);
    font-size: 36px;
    margin-right: 14px;
    vertical-align: 4px;
  }
  .details {
    position: absolute;
    top: 836px; left: 0; width: 100%;
    text-align: center;
    font-size: 29px;
    line-height: 41px;
    color: var(--yellow);
  }
  .quote-call {
    position: absolute;
    top: 988px; left: 0; width: 100%;
    text-align: center;
    font-size: 29px;
    line-height: 1;
    color: var(--yellow);
  }
  .contact-name {
    position: absolute;
    top: 1030px; left: 0; width: 100%;
    text-align: center;
    font-family: "Merriweather", serif;
    font-weight: 900;
    font-size: 56px;
    line-height: 1;
    color: var(--yellow);
  }
  .contact-phone {
    position: absolute;
    top: 1094px; left: 0; width: 100%;
    text-align: center;
    font-family: "Merriweather", serif;
    font-weight: 900;
    font-size: 68px;
    line-height: 1;
    letter-spacing: 1px;
    color: var(--white);
  }
</style>
</head>
<body>
  <main class="flyer">
    <h1 class="brand-title">Harbor Ledger</h1>

    <svg class="hero-image" viewBox="0 0 480 340" role="img" aria-label="Photo of a small toy house with an orange roof sitting on a fan of banknotes">
      <defs>
        <linearGradient id="notes-tone" x1="0" y1="0" x2="1" y2="0">
          <stop offset="0" stop-color="var(--note-pink)"/>
          <stop offset="0.5" stop-color="#c9b6d6"/>
          <stop offset="1" stop-color="var(--note-teal)"/>
        </linearGradient>
        <radialGradient id="house-tone" cx="0.45" cy="0.4" r="0.6">
          <stop offset="0" stop-color="var(--roof)"/>
          <stop offset="0.6" stop-color="#f3e9e1"/>
          <stop offset="1" stop-color="#f3e9e1" stop-opacity="0"/>
        </radialGradient>
      </defs>
      <ellipse cx="270" cy="255" rx="215" ry="75" fill="url(#notes-tone)" opacity="0.85"/>
      <ellipse cx="200" cy="140" rx="150" ry="130" fill="url(#house-tone)"/>
    </svg>

    <h2 class="headline">Realtor<br>Pay Day</h2>
    <p class="subline">upon Subject Removal</p>

    <h3 class="intro">Did you know?</h3>
    <ul class="benefits">
      <li>Fees 100% tax deductable</li>
      <li>Same Day Service</li>
      <li>Confidential</li>
      <li>Low Rates</li>
    </ul>

    <p class="details">Your money from 583917 B.C. Ltd.<br>and It can be directly deposited into<br>your bank account or delivered to your office</p>

    <p class="quote-call">For quote: call</p>
    <p class="contact-name">Glen Marsh</p>
    <p class="contact-phone">236 555 0147</p>
  </main>
</body>
</html>
```